Bright Path Flyer Design for Virtual Online Clinic. -5.5 x 8.5 inches (half sheet)

We need a clean, modern flyer design for Bright Path, a new virtual walk-in clinic based in British Columbia. The flyer will be used in libraries, pharmacies, and community centers to help residents easily access primary care through their Bright Path NFC access card.
The flyer will ask a question : NEED A DOCTOR? This should be large and attention grabbing.
The design should clearly feature a Bright Path card image (the access card) as the centerpiece and visually show how patients can use it to book appointments. The tone should feel trustworthy, healthcare-oriented, and community-friendly — clean fonts, clear spacing, and strong readability from a distance.

Side One: This card has the NFC Access Card.
NEED A DOCTOR? (Large Font, Attention Grabbing)
How to Book an Appointment using your Bright Path Card
Step 1: Tap Your Card on Your Phone
Hold your card near the back of your phone.
It will activate automatically — no app needed.
The Bright Path scheduler will open.
Step 2: Schedule Your Appointment
Select your clinical concern.
Choose your time window.
Register (only once).
Confirm your appointment.
Step 3: Relax, we’ll take care of the rest
A doctor will call during your scheduled time.
Once booked, you’ll be able to call our office.
No emails, no texts — just a real person.
It’s that simple.
Side Two:
About Bright Path
Created by Dr. Marcus Ferrigan
Bright Path was founded to make healthcare simple and convenient. Prescription renewals. Common infections. Medical notes. And so much more.
Our doctors can address 120+ health concerns virtually — providing quality care without the waiting room. No waiting rooms. Just real doctors providing real care.
Why Patients Choose Bright Path
Easy access – book and be seen from anywhere in BC.
Effortless booking – tap your Bright Path Card to begin.
Trusted physicians – every visit is with a licensed BC family doctor.
How It Works
Book your visit — choose a time window that fits your day.
Join the queue — you’ll be called when it’s your turn.
Speak directly with your doctor — simple, secure, and stress-free.
Convenient Care for Common Concerns

Additional Details.
Please find the domain to be launched soon. I've attached the NFC card file for review, it is 85.5 mm x 54 mm. The card will be glued to the flyer.
I've attached examples of flyers but they are not the look I am seeking and I am looking for creative solutions.
Thank you!
http://brightpath-example.test/

Adult Patients in British Columbia

Healthcare

• Looking for clean lines, uniform appearance, and high legibility i.e poppins

0054AA
0677BA
7BADD7
CADEEF
E8F1F8

• Need A Doctor?
• Elegant style, not too busy, clear layout.
• Clutter, look cheap - review examples.

```html
<!DOCTYPE html>
<html lang="en">
<head>
<meta charset="utf-8">
<title>Bright Path Flyer</title>
<link href="https://fonts.googleapis.com/css2?family=Rubik:wght@300;400;500;600;700&family=Allura&display=swap" rel="stylesheet">
<style>
  :root {
    --navy: #2a438c;
    --ink: #1f2a44;
    --sky-1: #e8f1f8;
    --sky-2: #cadeef;
    --white: #ffffff;
    --stage: #8a8a8a;
  }
  * { box-sizing: border-box; margin: 0; padding: 0; }
  html, body { width: 949px; height: 1200px; overflow: hidden; }
  body { background: var(--stage); font-family: "Rubik", sans-serif; color: var(--ink); position: relative; }

  .flyer { position: absolute; left: 117px; width: 715px; height: 462px; background: var(--white); overflow: hidden; border-bottom: 4px solid var(--navy); }
  .flyer--front { top: 110px; }
  .flyer--back { top: 643px; }
  .wave { position: absolute; left: 0; bottom: 0; width: 100%; height: 100%; }

  /* Front */
  .headline-band { position: absolute; top: 0; left: 0; width: 100%; height: 109px; background: var(--navy); display: flex; align-items: center; justify-content: center; }
  .headline { color: var(--white); font-weight: 700; font-size: 80px; letter-spacing: -2px; line-height: 1; padding-top: 6px; }
  .booking-title { position: absolute; left: 32px; top: 126px; font-size: 22.5px; font-weight: 500; line-height: 28px; color: var(--navy); }
  .booking-title strong { font-weight: 700; text-transform: uppercase; }
  .card-visual { position: absolute; left: 30px; top: 226px; width: 260px; height: 204px; border-radius: 12px; background: linear-gradient(160deg, var(--navy) 0%, #3d58a3 55%, var(--sky-2) 100%); }

  .step { position: absolute; left: 372px; width: 330px; }
  .step-badge { position: absolute; left: 0; top: 0; width: 56px; text-align: center; }
  .step-tag { display: inline-block; background: var(--navy); color: var(--white); font-size: 9.5px; font-weight: 500; padding: 2px 4px; border-radius: 2px 2px 0 0; }
  .step-icon { width: 54px; height: 54px; margin: -2px auto 0; border: 2.5px solid var(--navy); border-radius: 50%; background: var(--white); display: flex; align-items: center; justify-content: center; }
  .step-body { margin-left: 69px; }
  .step-title { font-size: 15px; font-weight: 500; color: var(--navy); margin-bottom: 4px; }
  .step-list { list-style: none; font-size: 11px; line-height: 16.5px; color: var(--ink); }
  .step-list li { position: relative; padding-left: 14px; }
  .step-list li::before { content: ""; position: absolute; left: 2px; top: 6px; border-left: 4px solid var(--navy); border-top: 2.5px solid transparent; border-bottom: 2.5px solid transparent; }

  /* Back */
  .about-band { position: absolute; top: 0; left: 0; width: 100%; height: 161px; background: var(--navy); color: var(--white); }
  .about-brand { position: absolute; left: 20px; top: 30px; width: 270px; text-align: center; }
  .about-label { font-size: 17px; font-weight: 300; }
  .about-name { display: flex; align-items: center; justify-content: center; gap: 8px; font-size: 38px; font-weight: 400; line-height: 1.2; margin: 4px 0 8px; }
  .about-name .mark { width: 14px; height: 14px; border-radius: 50%; background: var(--sky-2); }
  .about-founder { font-size: 15.5px; font-weight: 300; }
  .about-founder strong { font-weight: 500; }
  .about-divider { position: absolute; left: 306px; top: 35px; width: 1px; height: 108px; background: var(--sky-2); }
  .about-copy { position: absolute; left: 329px; top: 34px; width: 370px; font-size: 14px; line-height: 17px; font-weight: 300; }
  .about-copy p + p { margin-top: 9px; }

  .benefits { position: absolute; top: 186px; }
  .benefits--why { left: 32px; width: 290px; }
  .benefits--how { left: 397px; width: 270px; }
  .benefits-title { font-size: 25px; line-height: 31px; color: var(--navy); font-weight: 400; }
  .benefits-title strong { font-weight: 500; }
  .benefits--how .benefits-title { font-weight: 500; }
  .benefit-list { list-style: none; margin-top: 17px; }
  .benefit-list li { display: flex; gap: 11px; font-size: 15.5px; line-height: 18.5px; margin-bottom: 10px; }
  .benefits--why .benefit-list li > span { max-width: 240px; }
  .benefits--how .benefit-list li > span { max-width: 232px; }
  .benefit-list svg { flex: none; margin-top: 2px; }
  .benefit-lead { color: var(--navy); font-weight: 500; }
  .tagline { position: absolute; left: 0; width: 100%; top: 412px; text-align: center; font-family: "Allura", cursive; font-size: 36px; color: var(--navy); }
</style>
</head>
<body>

<section class="flyer flyer--front">
  <svg class="wave" viewBox="0 0 715 462" preserveAspectRatio="none" aria-hidden="true">
    <path d="M0 270 C180 220 300 330 470 300 C580 280 650 250 715 280 L715 462 L0 462 Z" fill="var(--sky-1)"/>
    <path d="M0 350 C200 300 360 390 520 330 C610 300 670 320 715 300 L715 462 L0 462 Z" fill="var(--sky-2)" opacity="0.55"/>
  </svg>

  <header class="headline-band"><h1 class="headline">NEED A DOCTOR?</h1></header>

  <h2 class="booking-title">How to Book an<br>Appointment using your<br><strong>Bright Path Card</strong></h2>

  <div class="card-visual" role="img" aria-label="Two Bright Path NFC access cards, front and back, shown overlapping"></div>

  <div class="step" style="top:137px">
    <div class="step-badge"><span class="step-tag">STEP 1</span>
      <div class="step-icon"><svg width="28" height="28" viewBox="0 0 28 28" fill="none" stroke="var(--navy)" stroke-width="1.6"><rect x="6" y="3" width="13" height="22" rx="2"/><rect x="10" y="10" width="14" height="9" rx="1.5" fill="var(--white)"/><path d="M12 15h10"/></svg></div>
    </div>
    <div class="step-body">
      <h3 class="step-title">Tap Your Card on Your Phone</h3>
      <ul class="step-list">
        <li>Hold your card near the back of your phone.</li>
        <li>It will activate automatically — no app needed.</li>
        <li>The Bright Path scheduler will open.</li>
      </ul>
    </div>
  </div>

  <div class="step" style="top:240px">
    <div class="step-badge"><span class="step-tag">STEP 2</span>
      <div class="step-icon"><svg width="28" height="28" viewBox="0 0 28 28" fill="none" stroke="var(--navy)" stroke-width="1.6"><rect x="3" y="5" width="19" height="18" rx="2"/><path d="M3 10h19M8 3v4M17 3v4M7 14h2M11 14h2M15 14h2M7 18h2M11 18h2"/><circle cx="21" cy="20" r="5" fill="var(--white)"/><path d="M18.5 20l2 2 3-3.5"/></svg></div>
    </div>
    <div class="step-body">
      <h3 class="step-title">Schedule Your Appointment</h3>
      <ul class="step-list">
        <li>Select your clinical concern.</li>
        <li>Choose your time window.</li>
        <li>Register (only once).</li>
        <li>Confirm your appointment.</li>
      </ul>
    </div>
  </div>

  <div class="step" style="top:343px">
    <div class="step-badge"><span class="step-tag">STEP 3</span>
      <div class="step-icon"><svg width="28" height="28" viewBox="0 0 28 28" fill="none" stroke="var(--navy)" stroke-width="1.6"><path d="M14 15 C8 10 9 5 12 5 C13 5 14 6 14 7 C14 6 15 5 16 5 C19 5 20 10 14 15Z"/><path d="M3 12 L3 19 L8 24 L12 24 L12 20 L7 15"/><path d="M25 12 L25 19 L20 24 L16 24 L16 20 L21 15"/></svg></div>
    </div>
    <div class="step-body">
      <h3 class="step-title">Relax, we’ll take care of the rest</h3>
      <ul class="step-list">
        <li>A doctor will call during your scheduled time.</li>
        <li>Once booked, you’ll be able to call our office.</li>
        <li>No emails, no texts — just a real person.</li>
        <li>It’s that simple.</li>
      </ul>
    </div>
  </div>
</section>

<section class="flyer flyer--back">
  <svg class="wave" viewBox="0 0 715 462" preserveAspectRatio="none" aria-hidden="true">
    <path d="M0 250 C160 220 300 300 460 250 C570 215 650 250 715 230 L715 462 L0 462 Z" fill="var(--sky-1)" opacity="0.7"/>
    <path d="M0 360 C180 320 360 400 540 350 C620 330 680 350 715 340 L715 462 L0 462 Z" fill="var(--sky-1)"/>
  </svg>

  <header class="about-band">
    <div class="about-brand">
      <p class="about-label">About</p>
      <p class="about-name"><span>Bright Path</span><span class="mark"></span></p>
      <p class="about-founder">Created by <strong>Dr. Marcus Ferrigan</strong></p>
    </div>
    <div class="about-divider"></div>
    <div class="about-copy">
      <p>Bright Path was founded to make healthcare simple and convenient. Prescription renewals. Common infections. Medical notes. And so much more.</p>
      <p>Our doctors can address 120+ health concerns virtually — providing quality care without the waiting room. No waiting rooms. Just real doctors providing real care.</p>
    </div>
  </header>

  <div class="benefits benefits--why">
    <h2 class="benefits-title">Why Patients<br><strong>Choose Bright Path</strong></h2>
    <ul class="benefit-list">
      <li><svg width="13" height="13" viewBox="0 0 14 14"><circle cx="7" cy="7" r="7" fill="var(--navy)"/><path d="M4 7.2l2 2 4-4.4" stroke="#fff" stroke-width="1.8" fill="none"/></svg><span><span class="benefit-lead">Easy access –</span> book and be seen from anywhere in BC.</span></li>
      <li><svg width="13" height="13" viewBox="0 0 14 14"><circle cx="7" cy="7" r="7" fill="var(--navy)"/><path d="M4 7.2l2 2 4-4.4" stroke="#fff" stroke-width="1.8" fill="none"/></svg><span><span class="benefit-lead">Effortless booking –</span> tap your Bright Path Card to begin.</span></li>
      <li><svg width="13" height="13" viewBox="0 0 14 14"><circle cx="7" cy="7" r="7" fill="var(--navy)"/><path d="M4 7.2l2 2 4-4.4" stroke="#fff" stroke-width="1.8" fill="none"/></svg><span><span class="benefit-lead">Trusted physicians –</span> every visit is with a licensed BC family doctor.</span></li>
    </ul>
  </div>

  <div class="benefits benefits--how">
    <h2 class="benefits-title">How It Works</h2>
    <ul class="benefit-list">
      <li><svg width="13" height="13" viewBox="0 0 14 14"><circle cx="7" cy="7" r="7" fill="var(--navy)"/><path d="M4 7.2l2 2 4-4.4" stroke="#fff" stroke-width="1.8" fill="none"/></svg><span><span class="benefit-lead">Book your visit –</span> choose a time window that fits your day.</span></li>
      <li><svg width="13" height="13" viewBox="0 0 14 14"><circle cx="7" cy="7" r="7" fill="var(--navy)"/><path d="M4 7.2l2 2 4-4.4" stroke="#fff" stroke-width="1.8" fill="none"/></svg><span><span class="benefit-lead">Join the queue–</span> you’ll be called when it’s your turn.</span></li>
      <li><svg width="13" height="13" viewBox="0 0 14 14"><circle cx="7" cy="7" r="7" fill="var(--navy)"/><path d="M4 7.2l2 2 4-4.4" stroke="#fff" stroke-width="1.8" fill="none"/></svg><span><span class="benefit-lead">Speak directly with your doctor –</span> simple, secure, and stress-free.</span></li>
    </ul>
  </div>

  <p class="tagline">Convenient Care for Common Concerns</p>
</section>

</body>
</html>
```